Robotic Physical Therapy office needs a Grand Opening Flyer

We need a Grand Opening flyer design for a robotic physical therapy office named Stellar Motion Therapy. We would like it to have a clean, classy, upscale feeling that gives potential clients a V.I.P. feeling. We would like to use the colors black, gray, and yellow (logo will be uploaded).

Event: Thursday, June 1st, 2023 from 12pm-6pm
location: 58274 Harlow Ave, Bloomfield Hills, MI 48319

Industry/Entity Type

Physical therapy

Font styles to use
Script

Colors

Designer to choose colors to be used in the design.

Requirements
Nice to have
• More of a vip feel for the invite

```html
<!DOCTYPE html>
<html lang="en">
<head>
<meta charset="utf-8">
<title>Stellar Motion Therapy – Grand Opening</title>
<link rel="stylesheet" href="https://fonts.googleapis.com/css2?family=Bebas+Neue&family=Lato:wght@700&family=Rubik:ital,wght@0,900;1,800&display=swap">
<style>
  :root {
    --ink: #363541;
    --sun: #f5db2e;
    --paper: #ffffff;
    --backdrop: #ebebeb;
  }
  html, body {
    margin: 0;
    padding: 0;
    width: 1200px;
    height: 1200px;
    overflow: hidden;
    background: var(--backdrop);
  }
  .canvas {
    width: 1200px;
    height: 1200px;
    display: flex;
    align-items: center;
    justify-content: center;
  }
  .flyer {
    width: 777px;
    height: 1100px;
    display: block;
    background: var(--paper);
  }
  .band-dark { fill: var(--ink); }
  .band-sun { fill: var(--sun); }
  .brand-mark { fill: var(--ink); }
  .brand-name {
    font-family: "Lato", sans-serif;
    font-weight: 700;
    font-size: 46px;
    fill: var(--ink);
  }
  .headline {
    font-family: "Bebas Neue", sans-serif;
    font-size: 392px;
  }
  .headline-shadow { fill: var(--sun); }
  .headline-face { fill: var(--ink); }
  .event-tag-frame { fill: var(--ink); }
  .event-tag-fill { fill: var(--sun); }
  .event-line {
    font-family: "Rubik", sans-serif;
    font-weight: 900;
  }
  .event-tag-text { fill: var(--ink); font-size: 66px; }
  .event-date { fill: var(--ink); font-size: 60px; }
  .event-time { fill: var(--sun); font-size: 54px; }
  .location-label, .location-address {
    font-family: "Rubik", sans-serif;
    font-style: italic;
    font-weight: 800;
    font-size: 31px;
  }
  .location-label { fill: var(--sun); }
  .location-address { fill: var(--paper); }
</style>
</head>
<body>
<main class="canvas">
  <svg class="flyer" viewBox="0 0 1080 1529" xmlns="http://www.w3.org/2000/svg" aria-label="Stellar Motion Therapy grand opening flyer">
    <!-- diagonal bands -->
    <polygon class="band-sun" points="0,330 1080,114 1080,407 0,625"/>
    <polygon class="band-dark" points="710,137 1080,63 1080,165 710,238"/>
    <polygon class="band-sun" points="0,960 1080,744 1080,1032 0,1249"/>
    <polygon class="band-dark" points="0,1249 480,1153 480,1115 996,1015 996,1048 1080,1031 1080,1319 710,1392 710,1456 345,1529 0,1529"/>
    <polygon class="band-sun" points="710,1392 1080,1319 1080,1420 710,1494"/>

    <!-- brand -->
    <circle class="brand-mark" cx="112" cy="145" r="42"/>
    <text class="brand-name" x="172" y="137">Stellar Motion</text>
    <text class="brand-name" x="172" y="190">Therapy</text>

    <!-- headline -->
    <g class="headline">
      <text class="headline-shadow" x="192" y="592" textLength="712" lengthAdjust="spacingAndGlyphs">GRAND</text>
      <text class="headline-face" x="176" y="584" textLength="712" lengthAdjust="spacingAndGlyphs">GRAND</text>
      <text class="headline-shadow" x="90" y="903" textLength="944" lengthAdjust="spacingAndGlyphs">OPENING</text>
      <text class="headline-face" x="72" y="895" textLength="944" lengthAdjust="spacingAndGlyphs">OPENING</text>
    </g>

    <!-- event details -->
    <g transform="rotate(-11.3 95 1090)">
      <rect class="event-tag-frame" x="95" y="1000" width="292" height="92"/>
      <rect class="event-tag-fill" x="107" y="1012" width="268" height="68"/>
      <text class="event-line event-tag-text" x="118" y="1073" textLength="248" lengthAdjust="spacingAndGlyphs">EVENT</text>
    </g>
    <text class="event-line event-date" transform="rotate(-11.3 104 1168)" x="104" y="1168" textLength="905" lengthAdjust="spacingAndGlyphs">THURSDAY, JUNE 1ST, 2023</text>
    <text class="event-line event-time" transform="rotate(-11.3 512 1180)" x="512" y="1180" textLength="466" lengthAdjust="spacingAndGlyphs">FROM 12PM-6PM</text>

    <!-- location -->
    <text class="location-label" x="85" y="1336">LOCATION:</text>
    <text class="location-address" x="85" y="1383">58274 HARLOW AVE,</text>
    <text class="location-address" x="85" y="1430">BLOOMFIELD HILLS, MI 48319</text>
  </svg>
</main>
</body>
</html>
```